Corrow Family Farm fresh honey jar label

I need a label for jars of honey harvested at our farm. These are for gifts and personal use. We are looking to incorporate our farm brand into the label. We would like the design to take the existing brand and add some element like bees, honey, flowers, or hives to indicate the contents. We want the design to feel homemade and authentic without feeling cheap or hoaky

Requirements
Must have
• The label must be made to fit a 1" x2" rectangular label. The label must include the attached family brand. The label must include the text "Corrow Family Farms" "Pinebrook, USA" "Farm Fresh Honey". The label will be printed on off-white paper
Nice to have
• It would be nice to have illustrations of bees or flowers around the logo or hives or honeycombs. The label should have a vintage feel
Should not have
• The label should not feel overly cartoonish or hoaky

```html
<!DOCTYPE html>
<html lang="en">
<head>
<meta charset="utf-8">
<title>Corrow Family Farms – Farm Fresh Honey Label</title>
<link href="https://fonts.googleapis.com/css2?family=Montserrat:wght@400;500;600;700&display=swap" rel="stylesheet">
<style>
  :root {
    --page: #ffffff;
    --paper: #ebe7da;
    --ink: #2b2a26;
    --ink-soft: #3d3b35;
    --pill: #d8d2bd;
    --rule: #cdc7b3;
    --bloom-deep: #c81f5e;
    --bloom-mid: #e45c92;
    --bloom-light: #f3b9cf;
  }
  * { box-sizing: border-box; margin: 0; padding: 0; }
  html, body {
    width: 670px; height: 1200px; overflow: hidden;
    background: var(--page);
    font-family: "Montserrat", sans-serif;
    color: var(--ink);
  }
  .label {
    position: absolute;
    left: 0; top: 400px;
    width: 670px; height: 400px;
    background: var(--paper);
  }
  .brand-mark {
    position: absolute;
    top: 30px; left: 0; width: 100%;
    display: flex; justify-content: center; align-items: center; gap: 7px;
  }
  .brand-mark .square {
    width: 14px; height: 14px; background: var(--ink);
  }
  .brand-mark .name {
    font-weight: 700; font-size: 26px; letter-spacing: 0.12em; color: var(--ink);
  }
  .brand-place {
    position: absolute; top: 84px; width: 100%;
    text-align: center; font-size: 6px; font-weight: 500; color: var(--ink);
  }
  .illustration {
    position: absolute;
    left: 222px; top: 94px; width: 203px; height: 188px;
    background:
      radial-gradient(ellipse closest-side at 50% 50%, var(--bloom-deep) 0%, var(--bloom-mid) 38%, var(--bloom-light) 70%, rgba(243,185,207,0) 100%);
  }
  .farm-name {
    position: absolute; top: 287px; width: 100%;
    text-align: center;
    font-weight: 600; font-size: 26px; letter-spacing: 0.2em;
    padding-left: 0.2em;
    color: var(--ink);
  }
  .farm-place {
    position: absolute; top: 316px; width: 100%;
    text-align: center;
    font-weight: 400; font-size: 12px; letter-spacing: 0.32em;
    padding-left: 0.32em;
    color: var(--ink-soft);
  }
  .info-row {
    position: absolute; top: 355px; left: 0; width: 100%; height: 16px;
  }
  .info-row .weight {
    position: absolute; top: 0;
    font-weight: 600; font-size: 13px; letter-spacing: 0.08em; line-height: 16px;
  }
  .weight-imperial { left: 30px; }
  .weight-metric { right: 28px; }
  .info-row .rule {
    position: absolute; left: 98px; width: 460px; top: 8px;
    height: 1px; background: var(--rule);
  }
  .info-row .contents {
    position: absolute; left: 264px; top: 0; width: 145px; height: 16px;
    border-radius: 8px; background: var(--pill);
    display: flex; align-items: center; justify-content: center;
    font-weight: 700; font-size: 7.5px; letter-spacing: 0.28em; padding-left: 0.28em;
  }
</style>
</head>
<body>
  <main class="label">
    <div class="brand-mark">
      <span class="square"></span>
      <span class="name">CORROW</span>
    </div>
    <p class="brand-place">PINEBROOK, LOUISIANA</p>

    <div class="illustration" role="img" aria-label="Watercolour illustration of a bumblebee beside a pink blossom with dripping paint"></div>

    <h1 class="farm-name">CORROW FAMILY FARMS</h1>
    <p class="farm-place">PINEBROOK, USA</p>

    <div class="info-row">
      <span class="weight weight-imperial">9OOZ</span>
      <span class="rule"></span>
      <span class="contents">FARM FRESH HONEY</span>
      <span class="weight weight-metric">500GM</span>
    </div>
  </main>
</body>
</html>
```